Brightmoor Partners Branding Revamp

We are a consulting company, looking for a way to display and promote our brand. We have 2 sides to the business- Brightmoor (financial) and Partners (cyber security). The financial side products relate to business necessities: card processing, website design/hosting/maintenance, VoIP phone systems. The cyber security side promotes a bundled package of 4 solutions: network vulnerability scan, dark web scan, anti-ransomeware/malware software, and image-level backups. We want people to understand that partnering with Brightmoor Partners gives them “Elevated Peace of Mind” (tagline). Current badge and logos uploaded.

Target Market(s)

Small businesses

Contact Information for Business Card

Lena Marwick, Vice President, lena@brightmoorpartners.example, 555-806-1937, www.brightmoorpartners.example

Requirements
Nice to have
• I do prefer the darker background for front and back

```html
<!DOCTYPE html>
<html lang="en">
<head>
<meta charset="utf-8">
<title>Brightmoor Partners – Business Cards</title>
<link rel="stylesheet" href="https://fonts.googleapis.com/css2?family=Michroma&family=Open+Sans:wght@400;600&display=swap">
<style>
  :root {
    --canvas: #ebebeb;
    --card-black: #0b0b0b;
    --paper-white: #ffffff;
    --brand-red: #e01f26;
    --brand-red-dark: #8e0c12;
    --text-light: #f2f2f2;
    --text-muted: #cfcfcf;
  }
  * { box-sizing: border-box; margin: 0; padding: 0; }
  html, body { width: 1200px; height: 800px; overflow: hidden; }
  body {
    background: var(--canvas);
    font-family: "Open Sans", Arial, sans-serif;
    position: relative;
  }
  .card {
    position: absolute;
    top: 257px;
    width: 500px;
    height: 286px;
    background: var(--card-black);
    overflow: hidden;
    box-shadow: 0 6px 18px rgba(0,0,0,0.18);
  }
  .card--contact { left: 70px; }
  .card--brand { left: 630px; }

  .card__art { position: absolute; inset: 0; }

  .contact-brand {
    position: absolute;
    left: 120px;
    top: 44px;
    width: 180px;
    text-align: center;
    font-family: "Michroma", sans-serif;
    font-size: 13px;
    line-height: 1.5;
    letter-spacing: 2px;
    color: var(--brand-red);
  }

  .person { position: absolute; left: 30px; top: 152px; color: var(--text-light); }
  .person__name { font-size: 15px; letter-spacing: 1.5px; font-weight: 400; text-transform: uppercase; }
  .person__title { font-size: 10px; color: var(--text-muted); margin-top: 1px; }

  .contact-list { position: absolute; left: 30px; top: 198px; list-style: none; }
  .contact-list__item {
    display: flex; align-items: center; gap: 12px;
    font-size: 13px; color: var(--text-light);
    height: 23px;
  }
  .contact-list__icon {
    width: 15px; height: 15px; background: var(--brand-red);
    display: flex; align-items: center; justify-content: center; border-radius: 2px;
  }

  .wordmark {
    position: absolute; inset: 0;
    display: flex; align-items: center; justify-content: center; gap: 18px;
  }
  .wordmark__square { width: 46px; height: 46px; background: var(--brand-red); }
  .wordmark__name {
    font-family: "Michroma", sans-serif;
    color: var(--paper-white);
    font-size: 26px;
    letter-spacing: 6px;
    line-height: 1.35;
  }
  .wordmark__name span { display: block; font-size: 13px; letter-spacing: 7px; }
</style>
</head>
<body>

  <section class="card card--contact" aria-label="Business card, contact side">
    <svg class="card__art" width="500" height="286" viewBox="0 0 500 286" aria-hidden="true">
      <defs>
        <linearGradient id="band-red" x1="0" y1="0" x2="1" y2="0">
          <stop offset="0" stop-color="#8e0c12"/>
          <stop offset="0.45" stop-color="#e01f26"/>
          <stop offset="0.7" stop-color="#b5141b"/>
          <stop offset="1" stop-color="#e01f26"/>
        </linearGradient>
        <linearGradient id="band-red-diag" x1="0" y1="0" x2="1" y2="1">
          <stop offset="0" stop-color="#e01f26"/>
          <stop offset="1" stop-color="#8e0c12"/>
        </linearGradient>
      </defs>
      <polygon points="0,0 318,0 400,108 0,108" fill="#ffffff"/>
      <polygon points="0,108 420,108 440,136 0,136" fill="url(#band-red)"/>
      <polygon points="332,0 352,0 438,116 418,116" fill="url(#band-red-diag)"/>
    </svg>

    <div class="contact-brand">Brightmoor Partners</div>

    <div class="person">
      <h1 class="person__name">Lena Marwick</h1>
      <p class="person__title">Vice President</p>
    </div>

    <ul class="contact-list">
      <li class="contact-list__item">
        <span class="contact-list__icon">
          <svg width="10" height="10" viewBox="0 0 10 10" aria-hidden="true"><path d="M2 1 L4 1 L4.6 3 L3.5 3.8 Q4.5 5.8 6.2 6.5 L7 5.4 L9 6 L9 8 Q9 9 8 9 Q1 8.5 1 2 Q1 1 2 1Z" fill="#fff"/></svg>
        </span>555-806-1937
      </li>
      <li class="contact-list__item">
        <span class="contact-list__icon">
          <svg width="10" height="10" viewBox="0 0 10 10" aria-hidden="true"><rect x="1" y="2" width="8" height="6" fill="none" stroke="#fff" stroke-width="1"/><path d="M1 2 L5 5.5 L9 2" fill="none" stroke="#fff" stroke-width="1"/></svg>
        </span>lena@brightmoorpartners.example
      </li>
      <li class="contact-list__item">
        <span class="contact-list__icon">
          <svg width="10" height="10" viewBox="0 0 10 10" aria-hidden="true"><circle cx="5" cy="5" r="4" fill="none" stroke="#fff" stroke-width="0.9"/><path d="M1 5 H9 M5 1 Q2.5 5 5 9 M5 1 Q7.5 5 5 9" fill="none" stroke="#fff" stroke-width="0.8"/></svg>
        </span>www.brightmoorpartners.example
      </li>
    </ul>
  </section>

  <section class="card card--brand" aria-label="Business card, brand side">
    <div class="wordmark">
      <span class="wordmark__square" aria-hidden="true"></span>
      <p class="wordmark__name">BRIGHTMOOR<span>PARTNERS</span></p>
    </div>
  </section>

</body>
</html>
```